Business Card and Letterhead Design Project

We need a business card template and letterhead designed for our new business.
Business Card
The information on the business card will be:
Logo
"slogan" - a simpler way to save ahead
Person's Name
Title
Phone Number
Email Address
Website
We strive to make everything SIMPLE so please keep that in mind.
If you want to design something that would go on an odd shaped business card, that is fine, we are up for any ideas.
The Letterhead would have:
logo
business address
phone
fax
website
Here is a link to our logo files: http://qlnk.example/7Rv2PwQ
we can provide the winning designer with higher quality files if needbe.

```html
<!DOCTYPE html>
<html lang="en">
<head>
<meta charset="utf-8">
<title>Sprouvest Stationery</title>
<link href="https://fonts.googleapis.com/css2?family=Open+Sans:wght@400;600&family=Quicksand:wght@700&family=Great+Vibes&display=swap" rel="stylesheet">
<style>
  :root {
    --bg: #ececec;
    --paper: #f7f7f7;
    --ink: #5a5a5a;
    --ink-dark: #4a4a4a;
    --brand-grey: #5c5c5c;
    --green: #8cb33e;
    --card-dark: #666767;
    --white: #ffffff;
  }
  * { box-sizing: border-box; margin: 0; padding: 0; }
  html, body { width: 1200px; height: 800px; overflow: hidden; background: var(--bg); }
  body { position: relative; font-family: "Open Sans", Arial, sans-serif; color: var(--ink); }

  .brand { display: flex; align-items: center; }
  .brand-dot { border-radius: 50%; background: var(--green); flex: none; }
  .brand-rule { width: 1px; background: var(--green); flex: none; }
  .brand-name { font-family: "Quicksand", "Open Sans", sans-serif; font-weight: 700; color: var(--brand-grey); line-height: 1; }

  /* Letterhead */
  .letterhead { position: absolute; left: 236px; top: 83px; width: 457px; height: 644px; background: var(--paper); }
  .letterhead .brand { position: absolute; left: 29px; top: 28px; }
  .letterhead .brand-dot { width: 32px; height: 32px; }
  .letterhead .brand-rule { height: 52px; margin: 0 12px 0 9px; }
  .letterhead .brand-name { font-size: 34px; }

  .letter-body { position: absolute; left: 54px; top: 143px; width: 370px; font-size: 8.2px; line-height: 12.2px; }
  .salutation { font-weight: 600; color: var(--ink-dark); margin-bottom: 11px; }
  .letter-body p { margin-bottom: 12px; }

  .signoff { position: absolute; left: 54px; top: 476px; }
  .signature { font-family: "Great Vibes", cursive; font-size: 26px; color: var(--ink-dark); line-height: 1; }
  .role { font-size: 8.5px; font-weight: 600; color: var(--ink); margin-top: -2px; }

  .letter-footer { position: absolute; left: 0; top: 605px; width: 179px; }
  .letter-footer .rule { height: 1px; background: var(--green); }
  .letter-footer .details { padding-left: 31px; padding-top: 5px; font-size: 6.4px; line-height: 8px; color: var(--ink-dark); }
  .letter-footer .web { color: var(--green); font-weight: 600; }

  /* Business card, back */
  .card-back { position: absolute; left: 769px; top: 443px; width: 196px; height: 110px; background: var(--card-dark); }
  .card-back .mark { position: absolute; left: 84px; top: 32px; width: 28px; height: 28px; border-radius: 50%; background: var(--green); }
  .card-back .line { position: absolute; left: 0; right: 0; top: 74px; height: 1px; background: var(--green); opacity: .8; }
  .card-back .slogan { position: absolute; left: 0; right: 0; top: 70px; text-align: center; font-size: 5px; line-height: 8px; font-weight: 600; color: var(--white); }
  .card-back .slogan span { background: var(--card-dark); padding: 0 3px; }

  /* Business card, front */
  .card-front { position: absolute; left: 765px; top: 611px; width: 198px; height: 116px; background: var(--white); }
  .card-front .brand { position: absolute; left: 20px; top: 25px; }
  .card-front .brand-dot { width: 18px; height: 18px; }
  .card-front .brand-rule { height: 28px; margin: 0 5px 0 5px; }
  .card-front .brand-name { font-size: 19px; }
  .card-front .person { position: absolute; left: 20px; top: 84px; font-size: 7.4px; color: var(--ink-dark); }
  .card-front .person small { font-size: 4.6px; }
  .card-front .contact { position: absolute; left: 20px; top: 98px; font-size: 4.6px; color: var(--ink); white-space: nowrap; }
  .card-front .contact .web { color: var(--green); font-weight: 600; }
</style>
</head>
<body>

<section class="letterhead">
  <div class="brand">
    <span class="brand-dot"></span>
    <span class="brand-rule"></span>
    <span class="brand-name">Sprouvest</span>
  </div>

  <div class="letter-body">
    <div class="salutation">Lorem Ipsum,</div>
    <p>Cras mattis consectetur purus sit amet fermentum. Etiam porta sem malesuada magna mollis euismod. Integer posuere erat a ante venenatis dapibus posuere velit aliquet. Cras justo odio, dapibus ac facilisis in, egestas eget quam. Aenean eu leo quam. Pellentesque ornare sem lacinia quam venenatis vestibulum.</p>
    <p>Vivamus sagittis lacus vel augue laoreet rutrum faucibus dolor auctor. Donec sed odio dui. Etiam porta sem malesuada magna mollis euismod. Morbi leo risus, porta ac consectetur ac, vestibulum at eros. Nullam id dolor id nibh ultricies vehicula ut id elit.</p>
    <p>Donec id elit non mi porta gravida at eget metus. Fusce dapibus, tellus ac cursus commodo, tortor mauris condimentum nibh, ut fermentum massa justo sit amet risus. Cras justo odio, dapibus ac facilisis in, egestas eget quam. Cum sociis natoque penatibus et magnis dis parturient montes, nascetur ridiculus mus.</p>
    <p>Cum sociis natoque penatibus et magnis dis parturient montes, nascetur ridiculus mus. Curabitur blandit tempus porttitor. Aenean lacinia bibendum nulla sed consectetur. Lorem ipsum dolor sit amet, consectetur adipiscing elit.</p>
    <p>Cras justo odio, dapibus ac facilisis in, egestas eget quam. Morbi leo risus, porta ac consectetur ac, vestibulum at eros. Duis mollis, est non commodo luctus, nisi erat porttitor ligula, eget lacinia odio sem nec elit. Integer posuere erat a ante venenatis dapibus posuere velit aliquet. Vivamus sagittis lacus vel augue laoreet rutrum faucibus dolor auctor.</p>
  </div>

  <div class="signoff">
    <div class="signature">Your Name</div>
    <div class="role">Company Director</div>
  </div>

  <footer class="letter-footer">
    <div class="rule"></div>
    <div class="details">
      T (555) 01 284 36 70 &nbsp;|&nbsp; F (555) 01 284 36 71<br>
      2140 Alder Ln. Fairview, CA 90000<br>
      <span class="web">www.sprouvest.example</span>
    </div>
  </footer>
</section>

<section class="card-back">
  <span class="mark"></span>
  <span class="line"></span>
  <div class="slogan"><span>a simpler way to save ahead</span></div>
</section>

<section class="card-front">
  <div class="brand">
    <span class="brand-dot"></span>
    <span class="brand-rule"></span>
    <span class="brand-name">Sprouvest</span>
  </div>
  <div class="person">DANA WHITFIELD <small>Operation Manager</small></div>
  <div class="contact">T: (555) 01 284 36 70 &nbsp;|&nbsp; dana@sprouvest.example &nbsp;|&nbsp; <span class="web">www.sprouvest.example</span></div>
</section>

</body>
</html>
```